Tour agency for FIT and groups need a business card design

We need a business card design for a tour agency company that is based in Perth called" BRISK NO", we aim to provide customise, unique and seamless travel arrangement for FIT and groups. We serve both high profile businessperson, government authorities, business partners, executives and investors. The name card should be more professional looking.
Updates

Project Deadline Extended Reason: Have some changes that needed to make, director will be back to office on Monday, sorry for the inconvenience cause. Added Saturday, May 6, 2017

Target Market(s)

High profile businessperson, government authorities, business partners, executives and investors.

Industry/Entity Type

Tourism

Contact Information for Business Card

Brisk NO
Level 1, 214 Marlowe Avenue, Dunreath NO, 6120
www.briskno.com.au

Font styles to use
Serif

Colors

Designer to choose colors to be used in the design.

Requirements
Must have
• My project must have a company logo
Nice to have
• a more professional and solid yet friendly name card design. We may want to include chinese name in the name card as well. Edge of the card can be filled with gold and we think that transparent name cards are interesting.

```html
<!DOCTYPE html>
<html lang="en">
<head>
<meta charset="utf-8">
<title>Brisk NO – Business Card</title>
<link href="https://fonts.googleapis.com/css2?family=Roboto:wght@400;500&display=swap" rel="stylesheet">
<style>
  :root {
    --backdrop: #4a3e37;
    --card: #1b1b1b;
    --ink: #ffffff;
    --ink-soft: #e6e6e6;
    --accent: #29a8e0;
    --emboss: #8c8c8c;
  }
  * { box-sizing: border-box; margin: 0; padding: 0; }
  html, body {
    width: 1200px; height: 1200px; overflow: hidden;
    background: var(--backdrop);
    font-family: "Roboto", Arial, sans-serif;
  }
  .sheet { position: relative; width: 1200px; height: 1200px; }
  .card {
    position: absolute; left: 214px; width: 772px; height: 440px;
    background: var(--card); border-radius: 18px;
    box-shadow: 0 6px 18px rgba(0,0,0,.45);
  }
  .card--front { top: 151px; }
  .card--back { top: 633px; }

  .brand {
    position: absolute; transform: translate(-50%, -50%);
    font-weight: 500; white-space: nowrap; letter-spacing: 1px;
  }
  .card--front .brand { left: 226px; top: 219px; font-size: 50px; color: var(--accent); }
  .card--back .brand { left: 386px; top: 220px; font-size: 66px; color: var(--emboss); }

  .divider {
    position: absolute; left: 387px; top: 100px; width: 2px; height: 240px;
    background: var(--accent);
  }
  .details { position: absolute; left: 422px; top: 86px; color: var(--ink); }
  .details__name { font-size: 31px; font-weight: 400; line-height: 1.2; }
  .details__title { font-size: 19.5px; color: var(--accent); line-height: 1.3; margin-top: 1px; }
  .details__company { font-size: 20px; margin-top: 21px; line-height: 1.3; }
  .details__address { font-size: 17.5px; color: var(--ink-soft); line-height: 26px; }
  .contacts { list-style: none; margin-top: 14px; }
  .contacts li {
    display: flex; align-items: center; gap: 7px;
    font-size: 17.5px; color: var(--ink-soft); line-height: 27px;
  }
  .contacts svg { width: 17px; height: 17px; flex: none; stroke: var(--accent); fill: none; stroke-width: 1.6; }
</style>
</head>
<body>
<main class="sheet">
  <section class="card card--front">
    <div class="brand">Brisk NO</div>
    <div class="divider"></div>
    <div class="details">
      <h1 class="details__name">Marcus Hale</h1>
      <p class="details__title">President &amp; CEO</p>
      <p class="details__company">Brisk NO</p>
      <p class="details__address">Level 1, 214 Marlowe Avenue<br>Dunreath NO, 6120</p>
      <ul class="contacts">
        <li>
          <svg viewBox="0 0 24 24"><path d="M5 3h4l2 5-2.5 1.5a11 11 0 0 0 6 6L16 13l5 2v4a2 2 0 0 1-2 2A17 17 0 0 1 3 5a2 2 0 0 1 2-2z"/></svg>
          000-000-0000
        </li>
        <li>
          <svg viewBox="0 0 24 24"><rect x="2.5" y="5" width="19" height="14" rx="1"/><path d="M3 6l9 7 9-7"/></svg>
          m.hale@briskno.com.au
        </li>
        <li>
          <svg viewBox="0 0 24 24"><circle cx="12" cy="12" r="9.5"/><ellipse cx="12" cy="12" rx="4" ry="9.5"/><path d="M2.5 12h19M4 7h16M4 17h16"/></svg>
          www.briskno.com.au
        </li>
      </ul>
    </div>
  </section>

  <section class="card card--back">
    <div class="brand">Brisk NO</div>
  </section>
</main>
</body>
</html>
```